CoinVale Landing Page | A free, personalized stock market email

We are looking for someone to revamp our landing page at https://coinvale.example . You should get to know the product and what it offers, and present new designs for our landing page. Feel free to use assets that currently exist on the page, as well as any new assets that you can put together. This landing page should make it obvious what the product does and aim to dramatically increase our conversion rate. We are looking for creativity, uniqueness, and clarity of purpose.

Target Market(s)

People who are invested in, or interested in being invested in, the stock market

Industry/Entity Type

Finance

Number of Pages Required

1 page

Font styles to use
Sans Serif

Requirements
Must have
• Creativity, sleek/minimal design, existing color palette and logos
Nice to have
• Effective copy
Should not have
• Clutter

```html
<!DOCTYPE html>
<html lang="en">
<head>
<meta charset="utf-8">
<title>CoinVale — A free, personalized stock market email</title>
<link href="https://fonts.googleapis.com/css2?family=Poppins:wght@400;500;600;700&display=swap" rel="stylesheet">
<style>
:root{
  --blue:#16a6ef;
  --blue-dark:#0a8fd6;
  --ink:#111418;
  --text:#2b2f33;
  --muted:#8a9096;
  --tint:#e1f1fb;
  --tint-soft:#eef7fd;
  --white:#ffffff;
  --green:#5fd06a;
  --green-soft:#bfeec3;
  --red:#e53935;
  --line:#e3e6e9;
}
*{box-sizing:border-box;margin:0;padding:0}
html,body{width:1200px;height:5296px;overflow:hidden}
body{font-family:'Poppins',sans-serif;color:var(--text);background:var(--white);position:relative}
.abs{position:absolute}
.hl{color:var(--blue)}
.art{position:absolute;background:linear-gradient(160deg,#f3f6f8,#e2e7eb);border-radius:18px}

/* logo */
.logo{display:flex;align-items:center;gap:12px;font-weight:600;color:var(--ink)}
.logo .dot{border-radius:50%;background:var(--blue)}
.site-header{position:absolute;top:0;left:0;width:1200px;height:144px;display:flex;justify-content:center;align-items:center}
.site-header .logo{font-size:40px}
.site-header .dot{width:40px;height:40px}

/* hero */
.hero{position:absolute;top:144px;left:0;width:1200px;height:979px;background:var(--tint)}
.hero h1{position:absolute;top:74px;width:100%;text-align:center;font-size:86px;font-weight:600;color:var(--ink);letter-spacing:-1px}
.hero h1 span{font-weight:400;color:var(--blue)}
.btn-dark{position:absolute;top:206px;left:415px;width:370px;height:98px;border-radius:16px;background:var(--ink);color:var(--white);font-size:25px;display:flex;align-items:center;justify-content:center}
.phone{position:absolute;top:370px;width:236px;height:493px;border:6px solid var(--ink);border-radius:28px;background:var(--white);overflow:hidden;padding:26px 18px 10px;font-size:8px;color:var(--ink)}
.phone::before{content:"";position:absolute;top:0;left:68px;width:88px;height:14px;background:var(--ink);border-radius:0 0 10px 10px}
.phone .top{display:flex;align-items:center;justify-content:center;gap:4px;font-size:9px;color:var(--blue);margin-bottom:14px;position:relative}
.phone .top .back{position:absolute;left:0;color:var(--ink)}
.phone .top i{width:8px;height:8px;border-radius:50%;background:var(--blue);display:block}
.phone h4{font-size:14px;font-weight:700;line-height:1.15;margin-bottom:10px}
.phone .row{display:flex;justify-content:space-between;align-items:center;border-bottom:1px solid var(--line);padding:8px 0}
.tog{width:18px;height:10px;border-radius:6px;background:#cfd3d6;position:relative}
.tog::after{content:"";position:absolute;top:1px;left:1px;width:8px;height:8px;border-radius:50%;background:var(--white)}
.tog.on{background:var(--green)}
.tog.on::after{left:9px}
.phone .label{font-size:7px;color:var(--muted);margin-top:14px}
.phone p{font-size:6.5px;line-height:1.4;margin:3px 0}
.phone u{font-size:7.5px}
.caption{position:absolute;top:886px;width:280px;text-align:center;font-size:20px;font-weight:600;color:var(--ink);line-height:1.35}

/* intro */
.bubble{position:absolute;top:1209px;left:483px;width:592px;height:347px;border-radius:50%;background:var(--tint);border:1px solid #b7d9ee;display:flex;align-items:center;justify-content:center;text-align:center;font-size:33px;font-weight:500;line-height:1.25;color:var(--ink);padding:0 112px}
.bubble-tail{position:absolute;top:1490px;left:650px}

/* story */
.story{position:absolute;top:1758px;left:0;width:1200px;height:987px;background:var(--tint-soft)}
.story h2{font-size:31px;font-weight:500;color:var(--ink);line-height:1.2}
.story p{font-size:15.5px;line-height:1.75;color:var(--text);margin-top:22px}

/* features */
.blue-block{position:absolute;top:2741px;left:1077px;width:123px;height:318px;background:var(--blue)}
.feature{position:absolute;left:90px;display:flex;gap:18px;width:620px}
.feature .icon{width:103px;height:103px;border-radius:50%;background:var(--blue);flex:none;display:flex;align-items:center;justify-content:center}
.feature h3{font-size:24px;font-weight:500;color:var(--ink);margin-top:6px}
.feature p{font-size:15px;line-height:1.7;margin-top:8px}
.stock-card{position:absolute;top:2813px;left:746px;width:330px;height:528px;background:var(--white);box-shadow:0 6px 22px rgba(0,0,0,.08);padding:18px 14px;font-size:11px;color:var(--ink)}
.stock-card .tick{display:flex;align-items:center;gap:10px;font-size:19px;font-weight:600;color:var(--blue-dark)}
.pill{background:#e7eaec;border-radius:12px;padding:2px 10px;color:var(--ink);font-size:16px}
.sect{font-size:10px;color:#b0b5ba;letter-spacing:.5px;margin-top:16px;padding-top:6px;border-top:1px solid var(--line)}
.chg{display:flex;gap:22px;margin-top:12px;font-size:13px;font-weight:500}
.chg small{display:block;font-size:9.5px;font-weight:400;margin-left:14px}
.up::before{content:"▲ ";color:var(--green);font-size:9px}
.down::before{content:"▼ ";color:var(--red);font-size:9px}
.rating{display:flex;align-items:center;gap:14px;margin-top:14px;padding-left:6px}
.buy{width:56px;height:56px;background:var(--green-soft);color:#3a9a45;display:flex;align-items:center;justify-content:center;font-size:12px}
.bars div{height:6px;background:var(--line);margin:6px 0;width:116px}
.bars .g{background:var(--green)}
.pct{font-size:11px;line-height:1.35;color:#555}
.tbl{margin:10px 12px 0;width:276px;font-size:11.5px;border-collapse:collapse}
.tbl th{text-align:left;font-weight:600;border-bottom:1px solid #999;padding:4px}
.tbl td{padding:8px 4px}
.news{display:flex;gap:10px;background:#f0f2f4;margin-top:10px;padding:8px}
.news .thumb{width:56px;height:48px;background:linear-gradient(135deg,#c9b8a4,#7d8c99);flex:none}

/* pricing */
.free{position:absolute;top:3413px;left:0;width:1200px;height:935px;background:var(--tint-soft)}
.free h2{position:absolute;top:116px;width:100%;text-align:center;font-size:52px;font-weight:600;color:var(--ink)}
.free p{position:absolute;top:212px;width:100%;text-align:center;font-size:20px;line-height:1.3}
.btn-blue{position:absolute;top:308px;left:393px;width:427px;height:89px;border-radius:22px;background:var(--blue);color:var(--white);font-size:25px;display:flex;align-items:center;justify-content:center}

/* blog */
.blog h2{position:absolute;top:4468px;width:100%;text-align:center;font-size:60px;font-weight:600;color:var(--ink)}
.post{position:absolute;top:4595px;width:500px;height:325px;background:var(--white);box-shadow:0 4px 18px rgba(0,0,0,.1);padding:70px 28px 0}
.post .date{font-size:14px}
.post h3{font-size:24px;font-weight:500;color:var(--ink);margin:6px 0 16px}
.post p{font-size:14.5px;line-height:1.75}
.post a{display:block;margin-top:14px;font-size:14.5px;color:var(--blue);text-decoration:underline}
.share{position:absolute;bottom:24px;right:28px;display:flex;gap:12px}
.share i{width:30px;height:30px;border:1px solid #d8dcdf;border-radius:50%;display:block}

/* footer */
.site-footer{position:absolute;top:4996px;left:0;width:1200px;height:300px;background:var(--tint)}
.site-footer .logo{position:absolute;top:68px;left:0;width:100%;justify-content:center;font-size:50px}
.site-footer .dot{width:48px;height:48px}
.foot-nav{position:absolute;top:160px;width:100%;text-align:center;font-size:14.5px;color:var(--ink);letter-spacing:.4px}
.foot-nav span{margin:0 14px;color:#666}
.foot-line{position:absolute;top:230px;left:86px;width:1028px;height:1px;background:#cbd8e0}
.social{position:absolute;top:208px;left:1036px;display:flex;gap:10px}
.social i{width:32px;height:32px;border-radius:50%;display:block}
.copy{position:absolute;top:250px;width:100%;text-align:center;font-size:13px;color:#444}
</style>
</head>
<body>

<header class="site-header">
  <div class="logo"><span class="dot"></span>CoinVale</div>
</header>

<section class="hero">
  <h1>Do less. <span>Know more.</span></h1>
  <div class="btn-dark">SIGN UP FOR FREE</div>

  <div class="phone" style="left:201px">
    <div class="top"><span class="back">←</span><i></i>CoinVale</div>
    <h4>Nortrix Corporation (NTRX)</h4>
    <div class="row" style="border:0;justify-content:flex-start;gap:8px">Toggle All <span class="tog on"></span></div>
    <div class="label">Data</div>
    <p>This data is always delivered.</p>
    <div class="row">Price <span class="tog on"></span></div>
    <div class="row">News <span class="tog on"></span></div>
    <div class="row">Analyst Ratings <span class="tog on"></span></div>
    <div class="label">Indicators</div>
    <p>Indicator data is only sent when the indicator is triggered.</p>
    <div class="row"><u>Volatility Bands</u> <span class="tog on"></span></div>
    <div class="row"><u>MACD</u> <span class="tog on"></span></div>
    <div class="row"><u>Relative Strength Index</u> <span class="tog on"></span></div>
  </div>

  <div class="phone" style="left:483px">
    <div class="top"><span class="back">←</span><i></i>CoinVale</div>
    <h4>Your Schedule</h4>
    <p>Currently, we only offer notifications during US market trading hours.</p>
    <p>Your timezone is: <b>America/New_York</b></p>
    <p><u>Change timezone</u></p>
    <div class="row">9:30 AM <span class="tog on"></span></div>
    <div class="row">10:00 AM <span class="tog"></span></div>
    <div class="row">10:30 AM <span class="tog on"></span></div>
    <div class="row">11:00 AM <span class="tog"></span></div>
    <div class="row">11:30 AM <span class="tog"></span></div>
    <div class="row">12:00 PM <span class="tog"></span></div>
    <div class="row">12:30 PM <span class="tog on"></span></div>
    <div class="row">1:00 PM <span class="tog"></span></div>
    <div class="row">1:30 PM <span class="tog"></span></div>
  </div>

  <div class="phone" style="left:763px">
    <div class="top" style="font-size:18px;color:var(--ink)"><i style="width:16px;height:16px"></i>CoinVale</div>
    <p style="text-align:center">4:30 PM, June 02 2023</p>
    <div style="margin-top:30px;font-size:11px;font-weight:600;color:var(--blue-dark)">NTRX <span class="pill" style="font-size:9px">$393.27</span></div>
    <p>Nortrix Corporation</p>
    <p>+1.11% · +39.41% · +108.92%</p>
    <div class="label">ANALYST RATINGS</div>
    <p>What 41 Wallstreet experts are saying:</p>
    <div style="display:flex;gap:8px;align-items:center"><div class="buy" style="width:30px;height:30px;font-size:7px">BUY</div><div style="flex:1;height:4px;background:var(--green)"></div><p>95.4% Buy</p></div>
    <div class="label">INDICATORS</div>
    <div class="row">Signal <span>Type</span></div>
    <p>Volatility Bands &nbsp; BUY</p>
    <div class="label">NEWS</div>
    <div style="display:flex;gap:6px;background:#f0f2f4;padding:5px"><span style="width:26px;height:22px;background:#9aa7b3;flex:none"></span><p><b>Dana Whitfield on Nortrix, AI Investments and US Economy</b></p></div>
    <div style="margin-top:26px;font-size:11px;font-weight:600;color:var(--blue-dark)">JRV <span class="pill" style="font-size:9px">$140.47</span></div>
  </div>

  <div class="caption" style="left:178px">Subscribe to asset notifications</div>
  <div class="caption" style="left:461px">Set your schedule</div>
  <div class="caption" style="left:741px">Get your email</div>
</section>

<section class="intro">
  <div class="art" style="left:216px;top:1254px;width:257px;height:483px" role="img" aria-label="Line drawing of the mascot in a suit, waving"></div>
  <div class="bubble"><div><span class="hl">CoinVale</span> is your free, personalized, data-driven finance email</div></div>
  <svg class="bubble-tail" width="70" height="70" viewBox="0 0 70 70" aria-hidden="true"><path d="M10 0 L0 70 L60 10 Z" fill="var(--tint)" stroke="#b7d9ee"/></svg>
</section>

<section class="story">
  <div class="art" style="left:612px;top:133px;width:441px;height:299px" role="img" aria-label="Sketch of the mascot relaxing in a beach chair with a drink under the sun"></div>
  <div class="abs" style="left:148px;top:170px;width:450px">
    <h2>Stop scanning <span class="hl">charts<br>and chasing data...</span></h2>
    <p>Don't bend over backwards to get the investment insights you need. You have better ways to spend your time and energy.</p>
  </div>
  <div class="art" style="left:195px;top:473px;width:250px;height:349px" role="img" aria-label="Sketch of the mascot standing and pointing at himself"></div>
  <div class="art" style="left:515px;top:290px;width:130px;height:100px" role="img" aria-label="Sketch of a winged envelope flying"></div>
  <div class="abs" style="left:473px;top:650px;width:480px">
    <h2>Let the information<br><span class="hl">come right to you</span></h2>
    <p>We'll send you curated market insights exactly when you want them.</p>
  </div>
</section>

<section class="features">
  <div class="blue-block"></div>

  <div class="feature" style="top:2870px">
    <div class="icon"><svg width="50" height="50" viewBox="0 0 50 50"><circle cx="25" cy="25" r="20" fill="none" stroke="#fff" stroke-width="4"/><path d="M25 13v12l-7 5" stroke="#fff" stroke-width="4" fill="none" stroke-linecap="round"/></svg></div>
    <div><h3>Your <span class="hl">Schedule</span></h3><p>Customize when you get your email. Up to every<br>half an hour during US market trading hours.</p></div>
  </div>
  <div class="feature" style="top:3002px">
    <div class="icon"><svg width="44" height="50" viewBox="0 0 44 50"><rect x="6" y="4" width="32" height="42" rx="3" fill="#fff"/><path d="M13 18h18M13 25h18M13 32h18M13 39h12" stroke="var(--blue)" stroke-width="3"/></svg></div>
    <div><h3>Your <span class="hl">Assets</span></h3><p>Choose from thousands of assets to include in<br>your email. GLX, JRV, ARVN and more!</p></div>
  </div>
  <div class="feature" style="top:3138px">
    <div class="icon"><svg width="50" height="50" viewBox="0 0 50 50"><rect x="8" y="6" width="34" height="12" rx="2" fill="#fff"/><rect x="4" y="22" width="42" height="22" rx="3" fill="#fff"/><path d="M12 30h26" stroke="var(--blue)" stroke-width="3"/></svg></div>
    <div><h3>All the <span class="hl">Data</span></h3><p>We provide as much data on assets as we can, including price,<br>price change, analyst ratings, technical indicators, and news.</p></div>
  </div>

  <div class="stock-card">
    <div class="tick">SLVN <span class="pill">$199.10</span></div>
    <div style="font-size:11px;color:#555;margin-top:2px">Solvane Energy, Inc.</div>
    <div class="chg">
      <div class="up">+2.89%<small>1-Day</small></div>
      <div class="down">−3.89%<small>30-Day</small></div>
      <div class="up">+10.67%<small>1-Year</small></div>
    </div>
    <div class="sect">ANALYST RATINGS</div>
    <div style="margin-top:6px;font-size:12px">What <b>35</b> Wallstreet experts are saying:</div>
    <div class="rating">
      <div class="buy">BUY</div>
      <div class="bars"><div class="g"></div><div></div><div style="width:60px"></div></div>
      <div class="pct">54.3% &nbsp;Buy<br>31.4% &nbsp;Hold<br>14.3% &nbsp;Sell</div>
    </div>
    <div style="display:flex;align-items:center;gap:8px;margin:14px 0 0 10px">
      <svg width="26" height="26" viewBox="0 0 26 26"><circle cx="13" cy="13" r="11" fill="none" stroke="var(--blue)" stroke-width="2"/><circle cx="13" cy="13" r="4" fill="var(--blue)"/></svg>
      <div style="font-size:9px;color:#777">Target Price<br><b style="font-size:13px;color:var(--ink)">$205</b></div>
    </div>
    <div class="sect">INDICATORS</div>
    <table class="tbl"><tr><th>Signal</th><th>Type</th></tr><tr><td>Volatility Bands</td><td>BUY</td></tr></table>
    <div class="sect">NEWS</div>
    <div class="news"><div class="thumb" role="img" aria-label="News thumbnail"></div><div style="font-size:12px;line-height:1.25">Top 10 Solar Stocks To Watch This Year<div style="font-size:9px;color:#999;margin-top:6px">By Lee Harlow via MarketWire</div></div></div>
  </div>
</section>

<section class="free">
  <h2>Stop paying for information</h2>
  <p>Don't spend a dime on financial information,<br>use that money for investments</p>
  <div class="btn-blue">CoinVale is free. Period.</div>
  <div class="art" style="left:181px;top:462px;width:841px;height:473px;border-radius:18px 18px 0 0" role="img" aria-label="Sketch of the mascot in tall grass chasing floating ticker symbols with a butterfly net"></div>
</section>

<section class="blog">
  <h2>Our <span class="hl">Blog</span></h2>
  <article class="post" style="left:86px">
    <div class="date">JUN 3, 2023</div>
    <h3>Volatility Bands</h3>
    <p>Financial markets can be a daunting realm for those unfamiliar with its jargon and concepts. Terms like "Volatility Bands" may sound perplexing, but fear not! In this article.</p>
    <a>Read More</a>
    <div class="share"><i></i><i></i></div>
  </article>
  <article class="post" style="left:615px">
    <div class="date">JUN 4, 2023</div>
    <h3>What are Technical Indicators?</h3>
    <p>This is a quick and dirty explanation of what technical indicators are, for those who are not already familiar. Does the term sound intimidating? Maybe a little.</p>
    <a>Read More</a>
    <div class="share"><i></i><i></i></div>
  </article>
</section>

<footer class="site-footer">
  <div class="art" style="left:119px;top:50px;width:103px;height:164px;border-radius:10px" role="img" aria-label="Small sketch of the mascot waving"></div>
  <div class="logo"><span class="dot"></span>CoinVale</div>
  <nav class="foot-nav">ABOUT<span>|</span>BLOG<span>|</span>TERMS OF USE<span>|</span>PRIVACY POLICY</nav>
  <div class="social"><i style="background:var(--ink)"></i><i style="background:var(--red)"></i></div>
  <div class="foot-line"></div>
  <div class="copy">Copyright © 2023 CoinVale LLC</div>
</footer>

</body>
</html>
```